TRUCK WASH OUTDOOR DRIVE THROUGH MENU CONTEST

WE NEED A DRIVE THROUGH MENU WITH OUR SERVICES AND PRICES. I HAVE ATTACHED A FEW EXAMPLES THAT I STARTED.

I WANT THIS TO BE EYE CATCHING WITH BRIGHT COLORS

Target Market(s)

TRUCK WASH AND DETAIL SHOP, TRANSPORTATION.

Requirements
Must have
• INCORPORATE MY LOGO INTO THE SIGN.
• FINAL PROJECT MUST BE IN .AI FORMAT.
• COMPANY COLORS ARE RED AND BLUE

```html
<!DOCTYPE html>
<html lang="en">
<head>
<meta charset="utf-8">
<title>Haulside Wash – Drive Through Menu</title>
<link href="https://fonts.googleapis.com/css2?family=Michroma&family=Russo+One&display=swap" rel="stylesheet">
<style>
  :root{
    --bg:#f4f6f3;
    --green-top:#9fd47d;
    --green-light:#8fd082;
    --green-gold:#77c143;
    --blue-band:#8ec9ec;
    --rose-band:#d8a89a;
    --magenta:#d24ea6;
    --magenta-dark:#9a4fa8;
    --orange:#f28c1e;
    --yellow:#fbc02d;
    --blue:#4b9ce0;
    --blue-dark:#3f78c8;
    --ink:#1f1f1f;
    --white:#ffffff;
    --red:#e02323;
    --logo:#e8505b;
  }
  html,body{margin:0;padding:0;overflow:hidden;background:var(--bg);}
  .menu{display:block;width:872px;height:1200px;}
  .heading{font-family:"Michroma",sans-serif;font-size:28px;fill:var(--white);letter-spacing:1px;}
  .service{font-family:"Michroma",sans-serif;font-size:21px;fill:var(--ink);}
  .price{font-family:"Michroma",sans-serif;font-size:28px;fill:var(--white);}
  .tier{font-family:"Russo One",sans-serif;font-size:34px;fill:var(--white);font-style:italic;}
  .brand{font-family:"Michroma",sans-serif;font-size:17px;fill:var(--logo);}
  .footer-note{font-family:"Michroma",sans-serif;font-size:19px;fill:var(--red);}
</style>
</head>
<body>
<svg class="menu" viewBox="0 0 872 1200" xmlns="http://www.w3.org/2000/svg" role="img" aria-label="Haulside Wash drive through price menu">
  <defs>
    <linearGradient id="sky" x1="0" y1="0" x2="0" y2="1">
      <stop offset="0" stop-color="#ffffff"/>
      <stop offset="1" stop-color="#eef0ee"/>
    </linearGradient>
    <linearGradient id="fold-orange" x1="0" y1="0" x2="1" y2="1">
      <stop offset="0" stop-color="var(--yellow)"/>
      <stop offset="1" stop-color="var(--orange)"/>
    </linearGradient>
  </defs>

  <!-- page background -->
  <rect class="page" width="872" height="1200" fill="url(#sky)"/>

  <!-- top green header wave -->
  <path class="header-wave" d="M0 0H872V120C700 60 520 150 330 170C190 185 70 140 0 110Z" fill="var(--green-top)"/>
  <path class="header-swoosh" d="M0 80C120 140 260 150 400 130C560 110 720 60 872 80V110C720 90 560 140 400 160C250 180 110 160 0 120Z" fill="#ffffff" opacity=".45"/>

  <!-- bottom green wave -->
  <path class="footer-wave" d="M0 1110C180 1160 420 1170 620 1150C740 1138 820 1120 872 1105V1200H0Z" fill="var(--green-top)"/>
  <path class="footer-swoosh" d="M0 1130C200 1175 450 1180 640 1160C760 1148 830 1132 872 1120V1140C820 1155 740 1170 630 1178C440 1192 200 1185 0 1150Z" fill="#ffffff" opacity=".5"/>

  <!-- brand mark -->
  <g class="brand-mark">
    <circle cx="140" cy="78" r="30" fill="var(--logo)"/>
    <text class="brand" x="140" y="142" text-anchor="middle">Haulside Wash</text>
  </g>

  <text class="heading" x="287" y="46">STANDARD TRACTOR &amp;</text>
  <text class="heading" x="287" y="88">TRAILER (53’)</text>

  <!-- EXPRESS tier -->
  <g class="tier-express">
    <polygon points="70,226 811,182 800,367 77,315" fill="var(--green-light)"/>
    <polygon points="243,142 387,121 432,223" fill="var(--magenta-dark)"/>
    <polygon points="387,201 475,137 454,238" fill="var(--magenta)"/>
    <polygon points="163,201 292,180 337,335 202,353" fill="var(--magenta)"/>
    <text class="price" x="202" y="294">$50</text>
    <text class="tier" x="325" y="296">EXPRESS</text>
    <text class="service" x="612" y="248">PRE-SOAK</text>
    <text class="service" x="612" y="287">SOAP</text>
    <text class="service" x="612" y="326">RINSE</text>
  </g>

  <!-- SILVER tier -->
  <g class="tier-silver">
    <polygon points="79,438 820,481 814,588 90,622" fill="var(--blue-band)"/>
    <polygon points="420,395 500,368 651,400 454,501" fill="url(#fold-orange)"/>
    <polygon points="600,438 735,460 690,610 555,610" fill="url(#fold-orange)"/>
    <text class="service" x="120" y="490">PRE-SOAK</text>
    <text class="service" x="120" y="526">SOAP &amp; SCRUB</text>
    <text class="service" x="120" y="561">RINSE</text>
    <text class="service" x="120" y="601">TIRE SHINE</text>
    <text class="tier" x="432" y="555">SILVER</text>
    <text class="price" x="592" y="553">$100</text>
  </g>

  <!-- GOLD tier -->
  <g class="tier-gold">
    <polygon points="67,728 808,685 797,874 75,815" fill="var(--green-gold)"/>
    <polygon points="238,646 365,619 465,646 443,748" fill="var(--blue-dark)"/>
    <polygon points="163,705 292,683 337,855 197,860" fill="var(--blue)"/>
    <text class="price" x="188" y="803">$150</text>
    <text class="tier" x="318" y="805">GOLD</text>
    <text class="service" x="561" y="732">PRE-SOAK</text>
    <text class="service" x="561" y="765">SOAP &amp; SCRUB</text>
    <text class="service" x="561" y="798">RINSE</text>
    <text class="service" x="561" y="834">TIRE SHINE</text>
    <text class="service" x="561" y="863">WET X POLISH</text>
  </g>

  <!-- PLATINUM tier -->
  <g class="tier-platinum">
    <polygon points="84,935 825,981 819,1074 95,1122" fill="var(--rose-band)"/>
    <polygon points="426,898 505,871 656,903 454,983" fill="url(#fold-orange)"/>
    <polygon points="611,935 741,962 696,1107 561,1107" fill="url(#fold-orange)"/>
    <text class="service" x="112" y="978">PRE-SOAK</text>
    <text class="service" x="112" y="1009">SOAP &amp; SCRUB</text>
    <text class="service" x="112" y="1042">RINSE</text>
    <text class="service" x="112" y="1075">TIRE SHINE</text>
    <text class="service" x="112" y="1107">PLATINUM PROTECT</text>
    <text class="tier" x="400" y="1052">PLATINUM</text>
    <text class="price" x="594" y="1050">$200</text>
  </g>

  <text class="footer-note" x="436" y="1187" text-anchor="middle">FOR MORE OPTIONS PLEASE ASK FRONT DESK</text>
</svg>
</body>
</html>
```